Poster Design

Hello,

My name is Rowan Pickett and I run a vidora channel called 'CrumbleDiary'. I want a poster made for those who watch my video to purchase and put on their wall at home. The poster will be all text and as you can see, I've attached a few examples of posters which I would like it to be similar to. I use a lot of the colour #ab6f7f so it would be good to incorporate this in somewhere (maybe the background colour).
I would like the poster to say:
"Do More Of What Makes YOU Happy"
I need this poster to be for sale ready for christmas, so Im going to need the designs created as soon as possible. Im sorry for the rush.
Have fun with it and feel free to upload multiple versions of a design as well as a few designs if you like.
I look forward to seeing what you come up with.
Rowan
(Of course I will need to own all rights once the payment has been made)

```html
<!DOCTYPE html>
<html lang="en">
<head>
<meta charset="utf-8">
<title>Do More Of What Makes You Happy — Poster</title>
<link rel="stylesheet" href="https://fonts.googleapis.com/css2?family=Italiana&family=Italianno&family=Russo+One&family=Special+Elite&display=swap">
<style>
  :root {
    --plum-deep: #5a1f4e;
    --plum: #7e2f5e;
    --rose: #ab6f7f;
    --coral: #d9654f;
    --orange: #e98a4a;
    --apricot: #f3b463;
    --sun: #f6c865;
    --ink-light: #ffffff;
    --glow: rgba(90, 20, 40, 0.45);
  }
  * { margin: 0; padding: 0; box-sizing: border-box; }
  html, body {
    width: 900px;
    height: 1200px;
    overflow: hidden;
    background: var(--plum-deep);
  }
  .poster {
    position: relative;
    width: 900px;
    height: 1200px;
    overflow: hidden;
  }
  .poster-backdrop {
    position: absolute;
    inset: 0;
    background:
      radial-gradient(ellipse 70% 55% at 78% 18%, var(--sun) 0%, var(--apricot) 30%, rgba(243,180,99,0) 70%),
      radial-gradient(ellipse 80% 60% at 45% 50%, var(--orange) 0%, rgba(233,138,74,0) 75%),
      radial-gradient(ellipse 60% 45% at 50% 85%, var(--coral) 0%, rgba(217,101,79,0) 80%),
      linear-gradient(160deg, var(--plum) 0%, var(--rose) 30%, var(--coral) 55%, var(--plum) 85%, var(--plum-deep) 100%);
  }
  .quote {
    position: absolute;
    inset: 0;
    color: var(--ink-light);
    text-align: center;
    text-shadow: 0 0 18px var(--glow), 0 0 4px var(--glow);
  }
  .quote span {
    position: absolute;
    left: 0;
    width: 100%;
    line-height: 1;
    white-space: nowrap;
  }
  .line-do-more {
    top: 88px;
    font-family: "Italiana", serif;
    font-size: 172px;
  }
  .line-of {
    top: 284px;
    font-family: "Italiana", serif;
    font-size: 100px;
  }
  .line-what-makes {
    top: 370px;
    font-family: "Italianno", cursive;
    font-size: 190px;
  }
  .line-you {
    top: 545px;
    font-family: "Russo One", sans-serif;
    font-size: 318px;
    letter-spacing: -6px;
  }
  .line-happy {
    top: 808px;
    font-family: "Special Elite", monospace;
    font-size: 232px;
    letter-spacing: 2px;
  }
</style>
</head>
<body>
  <main class="poster">
    <div class="poster-backdrop" role="img" aria-label="Low-poly geometric pattern background in purple, rose, orange and golden yellow"></div>
    <h1 class="quote">
      <span class="line-do-more">Do More</span>
      <span class="line-of">Of</span>
      <span class="line-what-makes">What Makes</span>
      <span class="line-you">YOU</span>
      <span class="line-happy">HAPPY</span>
    </h1>
  </main>
</body>
</html>
```